" A Construtora BAVO nasceu para tornar o setor da construçao civil mais industrializado e SUSTENTAVEL!!! Trouxe ao Brasil o sistema construtivo que é utilizado nos Estados Unidos e Europa. Com soluçoes inovadoras para a construçao de casas, aliando tecnologia e eficiência em produtos e serviços, Nosso foco de trabalho é a construçao de residências e imóveis comerciais em Steel Frame. A estrutura da casa inteira é feita usando aço leve galvanizado e perfis metálicos revestidos na area externa com placa cimenticia e internamente com placa de drywall "

```html
<!DOCTYPE html>
<html lang="pt-BR">
<head>
<meta charset="UTF-8">
<title>Construtora BAVO — Papel timbrado</title>
<link href="https://fonts.googleapis.com/css2?family=Montserrat:wght@500;700&display=swap" rel="stylesheet">
<style>
  :root {
    --backdrop: #e8e5e1;
    --paper: #ffffff;
    --brand-blue: #1f5470;
    --brand-green: #7ab52f;
    --watermark: #f1f2f3;
    --footer-text: #2f5c7a;
    --badge: #d3dadf;
  }
  html, body {
    margin: 0;
    padding: 0;
    width: 1200px;
    height: 1200px;
    overflow: hidden;
    background: var(--backdrop);
    font-family: "Montserrat", Arial, sans-serif;
  }
  .letterhead {
    position: absolute;
    left: 240px;
    top: 96px;
    width: 720px;
    height: 1008px;
    background: var(--paper);
    box-shadow: 0 4px 18px rgba(0,0,0,0.18);
    overflow: hidden;
  }
  .brand {
    position: absolute;
    top: 30px;
    left: 0;
    right: 0;
    display: flex;
    flex-direction: column;
    align-items: center;
  }
  .brand-row {
    display: flex;
    align-items: center;
    gap: 10px;
  }
  .brand-square {
    width: 30px;
    height: 30px;
    background: var(--brand-green);
  }
  .brand-name {
    font-weight: 700;
    font-size: 24px;
    letter-spacing: 1px;
    color: var(--brand-blue);
    text-transform: uppercase;
  }
  .brand-tagline {
    margin-top: 5px;
    font-weight: 500;
    font-size: 7px;
    letter-spacing: 0.8px;
    color: var(--brand-green);
    text-transform: uppercase;
  }
  .watermark {
    position: absolute;
    left: 30px;
    top: 560px;
    font-weight: 700;
    font-size: 230px;
    line-height: 1;
    letter-spacing: 4px;
    color: var(--watermark);
    text-transform: uppercase;
    white-space: nowrap;
  }
  .partner-badge {
    position: absolute;
    left: 12px;
    top: 950px;
    width: 100px;
    height: 34px;
    background: var(--badge);
  }
  .contact {
    position: absolute;
    left: 200px;
    width: 406px;
    top: 950px;
    text-align: center;
    color: var(--footer-text);
    font-weight: 500;
    font-size: 11.5px;
    line-height: 22px;
    white-space: nowrap;
  }
</style>
</head>
<body>
  <main class="letterhead">
    <header class="brand">
      <div class="brand-row">
        <span class="brand-square"></span>
        <span class="brand-name">Construtora BAVO</span>
      </div>
      <span class="brand-tagline">Construção industrializada e sustentável</span>
    </header>

    <div class="watermark" aria-hidden="true">BAVO</div>

    <footer>
      <div class="partner-badge" role="img" aria-label="Partner badge"></div>
      <div class="contact">
        <div class="contact-address">Rua das Acácias, 215 Jardim Aurora - Campinas SP - 11 4000-1234</div>
        <div class="contact-web">www.bavo.com.br</div>
      </div>
    </footer>
  </main>
</body>
</html>
```